FOLI PACK FOR STICKS

Design the packaging for salted sticks (weight 400g) reference to the logo VOLK (in attached).
Color packaging- look forward to suggestions.
Package with window.
Hi, we need only graphic conception without texts on back side.

Please find Logo VOLK and the grid of packaging - attached
Updates

Target Market(s)

typical salted snack for everyone (adults and children included)

Font styles to use
Sans Serif

Requirements
Should not have
• - religion and politic signs…
• - toys and childdraws
• - monsters, devils and demons etc.

```html
<!DOCTYPE html>
<html lang="en">
<head>
<meta charset="utf-8">
<title>VOLK Salt Sticks – 400g pack</title>
<link rel="stylesheet" href="https://fonts.googleapis.com/css2?family=Roboto+Condensed:wght@700&family=PT+Serif:wght@700&display=swap">
<style>
  :root {
    --paper: #ffffff;
    --gold-light: #d8a845;
    --gold: #c18d34;
    --gold-deep: #a8762a;
    --frame-gold: #e0b048;
    --brown: #6b4420;
    --brown-dark: #5a391c;
    --stick-light: #d9a35a;
    --stick-dark: #6a4218;
    --salt: #e6eaed;
    --wheat-light: #e3b96a;
    --wheat-mid: #d2a14c;
  }
  * { box-sizing: border-box; margin: 0; padding: 0; }
  html, body { width: 1200px; height: 1000px; overflow: hidden; background: var(--paper); }
  .canvas { position: relative; width: 1200px; height: 1000px; }

  .pack-body { position: absolute; left: 383px; top: 148px; width: 443px; height: 578px; }
  .pack-body svg { display: block; }

  .wheat-field {
    position: absolute; top: 252px; height: 470px;
    background: linear-gradient(180deg, var(--wheat-light) 0%, var(--wheat-mid) 50%, var(--wheat-light) 100%);
    opacity: .55;
  }
  .wheat-field--left { left: 387px; width: 108px; }
  .wheat-field--right { left: 722px; width: 100px; }
  .wheat-field--bottom { left: 495px; width: 227px; top: 630px; height: 92px; }

  .top-band {
    position: absolute; left: 503px; top: 155px; width: 210px; height: 130px;
    background: linear-gradient(180deg, var(--brown-dark), var(--brown));
  }
  .band-rails {
    position: absolute; left: 500px; top: 150px; width: 216px; height: 460px;
    border-left: 3px solid var(--frame-gold); border-right: 3px solid var(--frame-gold);
    opacity: .55;
  }

  .label {
    position: absolute; left: 510px; top: 262px; width: 196px; height: 334px;
    background: var(--frame-gold); border-radius: 12px;
  }
  .label-inner {
    position: absolute; inset: 4px; background: var(--paper); border-radius: 9px;
  }
  .brand {
    position: absolute; left: 0; right: 0; top: 18px; text-align: center;
    font-family: "Roboto Condensed", "Arial Narrow", sans-serif; font-weight: 700;
    font-size: 46px; letter-spacing: 1px; color: var(--brown);
  }
  .window {
    position: absolute; left: 4px; top: 80px; width: 180px; height: 168px;
    border-radius: 40px / 26px;
    background: linear-gradient(90deg, var(--stick-dark) 0%, var(--stick-light) 10%, var(--stick-dark) 18%,
      var(--stick-light) 28%, var(--stick-dark) 36%, var(--stick-light) 46%, var(--stick-dark) 54%,
      var(--stick-light) 64%, var(--stick-dark) 72%, var(--stick-light) 82%, var(--stick-dark) 90%, var(--stick-light) 100%);
    border: 3px solid var(--frame-gold);
  }
  .product-name {
    position: absolute; left: 0; right: 0; top: 258px; text-align: center;
    font-family: "Roboto Condensed", "Arial Narrow", sans-serif; font-weight: 700;
    color: var(--brown); line-height: 1;
  }
  .product-name .flavour { display: block; font-size: 18px; }
  .product-name .kind { display: block; font-size: 42px; margin-top: 1px; }

  .weight {
    position: absolute; left: 520px; top: 594px;
    font-family: "PT Serif", Georgia, serif; font-weight: 700; font-size: 24px;
    color: var(--paper);
    text-shadow: 0 0 2px var(--brown-dark), 0 0 2px var(--brown-dark);
  }
  .salt-heap {
    position: absolute; left: 664px; top: 556px; width: 92px; height: 74px;
    border-radius: 50%;
    background: radial-gradient(ellipse at 50% 55%, var(--paper) 0%, var(--salt) 55%, rgba(230,234,237,0) 100%);
  }
</style>
</head>
<body>
<main class="canvas">
  <div class="pack-body" role="img" aria-label="Golden foil bag">
    <svg width="443" height="578" viewBox="0 0 443 578">
      <defs>
        <linearGradient id="foil" x1="0" y1="0" x2="1" y2="1">
          <stop offset="0" stop-color="#c99436"/>
          <stop offset=".5" stop-color="#d8a845"/>
          <stop offset="1" stop-color="#b8842e"/>
        </linearGradient>
      </defs>
      <path fill="url(#foil)" d="M0 10 L6 2 L12 10 L18 2 L24 10 L30 2 L36 10 L42 2 L48 10 L54 2 L60 10 L66 2 L72 10 L78 2 L84 10 L90 2 L96 10 L102 2 L108 10 L114 2 L120 10 L126 2 L132 10 L138 2 L144 10 L150 2 L156 10 L162 2 L168 10 L174 2 L180 10 L186 2 L192 10 L198 2 L204 10 L210 2 L216 10 L222 2 L228 10 L234 2 L240 10 L246 2 L252 10 L258 2 L264 10 L270 2 L276 10 L282 2 L288 10 L294 2 L300 10 L306 2 L312 10 L318 2 L324 10 L330 2 L336 10 L342 2 L348 10 L354 2 L360 10 L366 2 L372 10 L380 2 L405 4 L430 30 L443 60 L443 578 L0 578 Z"/>
    </svg>
  </div>

  <div class="wheat-field wheat-field--left" role="img" aria-label="Repeating wheat ear pattern"></div>
  <div class="wheat-field wheat-field--right" role="img" aria-label="Repeating wheat ear pattern"></div>
  <div class="wheat-field wheat-field--bottom" role="img" aria-label="Repeating wheat ear pattern"></div>

  <div class="top-band" role="img" aria-label="Brown band with small repeated brand name pattern"></div>
  <div class="band-rails"></div>

  <section class="label">
    <div class="label-inner">
      <div class="brand">VOLK</div>
      <div class="window" role="img" aria-label="Window showing baked salt sticks"></div>
      <h1 class="product-name">
        <span class="flavour">SALT</span>
        <span class="kind">STICKS</span>
      </h1>
    </div>
  </section>

  <p class="weight">400g ℮</p>
  <div class="salt-heap" role="img" aria-label="Illustration of a small heap of salt"></div>
</main>
</body>
</html>
```